Employee Benefits and Insurance Consulting

We are an existing company with over 30 years experience but are changing our name. We would like a simple design with grey tones.

Industry/Entity Type

Insurance

Contact Information for Business Card

Crestwell Benefits Consulting
Gregory L Marsh CEO
5172 Pembrook Road
Harlow Ridge, TN 37990
greg@crestwellbc-example.com
555-412-3956 - O
555-547-2081 - C

```html
<!DOCTYPE html>
<html lang="en">
<head>
<meta charset="utf-8">
<title>Crestwell Benefits Consulting – Business Card</title>
<link rel="stylesheet" href="https://fonts.googleapis.com/css2?family=Arimo&family=Marcellus&family=Playfair+Display:ital@1&display=swap">
<style>
  :root {
    --page: #ffffff;
    --card: #e8f1f0;
    --band-grey: #899a99;
    --band-cyan: #56dffd;
    --divider: #7f9394;
    --ink-grey: #6f8385;
    --ink-name: #6b7f80;
    --ink-body: #4f5a5b;
    --accent: #4fcff0;
  }
  * { margin: 0; padding: 0; box-sizing: border-box; }
  html, body { width: 1200px; height: 702px; overflow: hidden; background: var(--page); }
  .canvas { position: relative; width: 1200px; height: 702px; }
  .card {
    position: absolute; left: 42px; top: 44px; width: 1116px; height: 616px;
    background: var(--card);
    box-shadow: 0 1px 3px rgba(0,0,0,0.18);
    overflow: hidden;
  }
  .band { position: absolute; height: 53px; }
  .band--top-left { left: 0; top: 0; width: 558px; background: var(--band-grey); }
  .band--top-right { left: 558px; top: 0; width: 558px; background: var(--band-cyan); }
  .band--bottom-left { left: 0; bottom: 0; width: 560px; background: var(--band-cyan); }
  .band--bottom-right { left: 560px; bottom: 0; width: 556px; background: var(--band-grey); }
  .glow {
    position: absolute; left: 40px; top: 70px; width: 480px; height: 460px;
    border-radius: 50%;
    background: radial-gradient(circle, rgba(240,246,245,0.9) 0%, rgba(232,241,240,0) 70%);
  }
  .divider { position: absolute; left: 560px; top: 67px; width: 3px; height: 487px; background: var(--divider); }

  .brand { position: absolute; left: 20px; width: 520px; top: 190px; text-align: center; }
  .brand__dot { display: block; width: 64px; height: 64px; margin: 0 auto 34px; border-radius: 50%; background: var(--band-cyan); }
  .brand__name { font-family: "Marcellus", serif; font-weight: 400; font-size: 46px; line-height: 1.2;
    color: var(--ink-grey); letter-spacing: 0.5px; }

  .person { position: absolute; left: 620px; width: 460px; top: 160px; text-align: center; }
  .person__name { font-family: "Marcellus", serif; font-size: 40px; color: var(--ink-name); line-height: 1.1; }
  .person__title { font-family: "Playfair Display", serif; font-style: italic; font-size: 21px; color: var(--accent); margin-top: 2px; margin-right: 14px; }

  .contacts { position: absolute; left: 730px; top: 280px; list-style: none;
    font-family: "Arimo", sans-serif; font-size: 20px; color: var(--ink-body); white-space: nowrap; }
  .contacts__item { display: flex; align-items: center; height: 33px; }
  .contacts__icon { width: 28px; height: 26px; margin-right: 12px; flex: none; }

  .address { position: absolute; left: 731px; top: 437px; font-family: "Arimo", sans-serif; font-style: normal;
    font-size: 20px; line-height: 30px; color: var(--ink-body); white-space: nowrap; }
</style>
</head>
<body>
<div class="canvas">
  <div class="card">
    <div class="band band--top-left"></div>
    <div class="band band--top-right"></div>
    <div class="band band--bottom-left"></div>
    <div class="band band--bottom-right"></div>
    <div class="glow"></div>
    <div class="divider"></div>

    <div class="brand">
      <span class="brand__dot"></span>
      <div class="brand__name">Crestwell<br>Benefits Consulting</div>
    </div>

    <div class="person">
      <div class="person__name">Gregory L Marsh</div>
      <div class="person__title">(CEO)</div>
    </div>

    <ul class="contacts">
      <li class="contacts__item">
        <svg class="contacts__icon" viewBox="0 0 28 26" aria-hidden="true">
          <circle cx="13" cy="13" r="11.5" fill="none" stroke="var(--band-cyan)" stroke-width="2"/>
          <rect x="9" y="6" width="8" height="14" rx="1.5" fill="none" stroke="var(--band-cyan)" stroke-width="1.6"/>
          <rect x="10.5" y="8" width="5" height="5" fill="var(--band-cyan)"/>
        </svg>
        <span>555-547-2081</span>
      </li>
      <li class="contacts__item">
        <svg class="contacts__icon" viewBox="0 0 28 26" aria-hidden="true">
          <circle cx="13" cy="13" r="12" fill="var(--band-cyan)"/>
          <path d="M9 7c1-.6 1.8-.3 2.3.6l1 2c.3.7 0 1.3-.5 1.7l-.7.5c.6 1.6 1.7 2.8 3.2 3.5l.6-.7c.5-.5 1.1-.7 1.7-.4l2 1c.8.4 1 1.3.4 2.2-.8 1.2-2.2 1.6-3.6 1-3.3-1.3-5.6-3.7-6.8-7-.5-1.5-.1-2.8.4-3.4z" fill="#ffffff"/>
        </svg>
        <span>555-412-3956</span>
      </li>
      <li class="contacts__item">
        <svg class="contacts__icon" viewBox="0 0 28 26" aria-hidden="true">
          <rect x="0" y="6" width="26" height="15" fill="var(--band-cyan)"/>
          <path d="M0 6l13 9 13-9" fill="none" stroke="#ffffff" stroke-width="1.6"/>
        </svg>
        <span>greg@crestwellbc-example.com</span>
      </li>
    </ul>

    <address class="address">
      5172 Pembrook Road<br>
      Harlow Ridge, TN 37990
    </address>
  </div>
</div>
</body>
</html>
```